RW Marlo Building Company LLC
Residential and Commercial Construction
I need double sided standard sized Business Card [3.5" x 2"]
Designer to decide.
Professional
Kevin R. Darrow
4815 Brindlecove Road
Harlow Springs, NC 27099
rw@rwmbuilding.example
My personal name does not need to be on the card or stationary since it is used in the company name.
New Home Construction,
Remodeling,
Room Additions,
Commercial Construction and Upfits,
Personalized Project Management

```html
<!DOCTYPE html>
<html lang="en">
<head>
<meta charset="utf-8">
<title>RW Marlo Building Company LLC — Stationery Set</title>
<link rel="stylesheet" href="https://fonts.googleapis.com/css2?family=Cinzel:wght@700&family=Open+Sans:wght@400;600&display=swap">
<style>
  :root {
    --stage: #e9e6e2;
    --paper: #ffffff;
    --ink: #1c1c1c;
    --muted: #6a6a6a;
    --red: #b3151c;
    --red-deep: #6e0a0e;
    --black: #151515;
    --faint: #e6e6e6;
  }
  * { box-sizing: border-box; margin: 0; padding: 0; }
  html, body { width: 1200px; height: 672px; overflow: hidden; }
  body {
    background: var(--stage);
    font-family: "Open Sans", Arial, sans-serif;
    color: var(--ink);
    position: relative;
  }
  .sheet {
    position: absolute;
    background: var(--paper);
    overflow: hidden;
    box-shadow: 0 2px 6px rgba(0,0,0,.18);
  }
  .wave { position: absolute; left: 0; bottom: 0; width: 100%; display: block; }
  .wave .band-black { fill: var(--black); }
  .wave .band-red { fill: url(#redBand); }

  .brand {
    font-family: "Cinzel", Georgia, serif;
    font-weight: 700;
    color: var(--ink);
    line-height: 1.05;
    letter-spacing: .02em;
  }
  .brand .mark {
    display: inline-block;
    width: .7em; height: .7em;
    background: var(--red);
    margin-right: .35em;
    vertical-align: middle;
  }
  .small { font-size: 6px; line-height: 1.45; color: var(--muted); white-space: nowrap; }

  /* business cards */
  .card { left: 84px; width: 182px; height: 100px; }
  .card--front { top: 163px; }
  .card--front .brand { position: absolute; left: 10px; top: 34px; font-size: 8px; width: 88px; }
  .card--front .contact { position: absolute; left: 104px; top: 18px; }
  .card--back { top: 283px; }
  .card--back .brand { position: absolute; left: 10px; top: 10px; font-size: 7px; white-space: nowrap; }
  .services { list-style: none; font-size: 5.6px; line-height: 1.5; white-space: nowrap; }
  .card--back .services { position: absolute; left: 12px; top: 32px; color: var(--ink); }
  .services li::before { content: "\25A0"; color: var(--red); margin-right: 3px; font-size: 4px; vertical-align: middle; }
  .card--red {
    top: 408px;
    background: linear-gradient(120deg, var(--red) 0%, var(--red-deep) 100%);
  }
  .card--red .brand { position: absolute; right: 10px; top: 10px; font-size: 7px; color: rgba(255,255,255,.3); white-space: nowrap; }
  .card--red .services { position: absolute; left: 12px; top: 36px; color: #fff; }
  .card--red .services li::before { color: #fff; }

  /* letterhead */
  .letterhead { left: 312px; top: 100px; width: 318px; height: 476px; }
  .letterhead .brand { position: absolute; left: 24px; top: 22px; font-size: 12px; width: 160px; }
  .letterhead .contact { position: absolute; left: 220px; top: 22px; }
  .letterhead .watermark {
    position: absolute; left: 84px; top: 190px;
    font-size: 14px; color: var(--faint); width: 170px;
  }
  .letterhead .watermark .mark { background: var(--faint); }

  /* envelopes */
  .envelope { left: 667px; width: 342px; }
  .envelope--flap { top: 211px; height: 149px; }
  .envelope--flap .flap { position: absolute; inset: 0; width: 100%; height: 100%; }
  .envelope--flap .brand { position: absolute; left: 50%; top: 22px; transform: translateX(-50%); font-size: 8px; text-align: center; white-space: nowrap; }
  .envelope--front { top: 372px; height: 137px; }
  .envelope--front .brand { position: absolute; left: 16px; top: 26px; font-size: 9px; width: 130px; }
  .envelope--front .contact { position: absolute; left: 16px; top: 56px; }
</style>
</head>
<body>

<svg width="0" height="0" aria-hidden="true" style="position:absolute">
  <defs>
    <linearGradient id="redBand" x1="0" x2="1" y1="0" y2="0">
      <stop offset="0" stop-color="#6e0a0e"/>
      <stop offset=".5" stop-color="#c0161e"/>
      <stop offset="1" stop-color="#7a0c10"/>
    </linearGradient>
  </defs>
</svg>

<section class="sheet card card--front">
  <div class="brand"><span class="mark"></span>RW Marlo Building Company LLC</div>
  <div class="contact small">
    4815 Brindlecove Road<br>
    Harlow Springs, NC 27099<br>
    P 336-555-0142<br>
    F 336-555-0143<br>
    rw@rwmbuilding.example
  </div>
  <svg class="wave" viewBox="0 0 100 20" preserveAspectRatio="none" height="22">
    <path class="band-black" d="M0 12 C30 4 60 18 100 6 L100 20 L0 20 Z"/>
    <path class="band-red" d="M0 15 C30 8 60 20 100 10 L100 20 L0 20 Z"/>
  </svg>
</section>

<section class="sheet card card--back">
  <div class="brand">RW Marlo Building Company LLC</div>
  <ul class="services">
    <li>New Home Construction</li>
    <li>Remodeling</li>
    <li>Room Additions</li>
    <li>Commercial Construction and Upfits</li>
    <li>Personalized Project Management</li>
  </ul>
  <svg class="wave" viewBox="0 0 100 20" preserveAspectRatio="none" height="16">
    <path class="band-black" d="M0 12 C30 4 60 18 100 6 L100 20 L0 20 Z"/>
    <path class="band-red" d="M0 15 C30 8 60 20 100 10 L100 20 L0 20 Z"/>
  </svg>
</section>

<section class="sheet card card--red">
  <div class="brand">RW Marlo Building Company LLC</div>
  <ul class="services">
    <li>New Home Construction</li>
    <li>Remodeling</li>
    <li>Room Additions</li>
    <li>Commercial Construction and Upfits</li>
    <li>Personalized Project Management</li>
  </ul>
</section>

<section class="sheet letterhead">
  <div class="brand"><span class="mark"></span>RW Marlo Building Company LLC</div>
  <div class="contact small">
    4815 Brindlecove Road<br>
    Harlow Springs, NC 27099<br>
    P 336-555-0142<br>
    F 336-555-0143<br>
    rw@rwmbuilding.example
  </div>
  <div class="brand watermark"><span class="mark"></span>RW Marlo Building Company LLC</div>
  <svg class="wave" viewBox="0 0 100 20" preserveAspectRatio="none" height="60">
    <path class="band-black" d="M0 8 C35 2 65 16 100 4 L100 20 L0 20 Z"/>
    <path class="band-red" d="M0 11 C35 6 65 19 100 8 L100 20 L0 20 Z"/>
  </svg>
</section>

<section class="sheet envelope envelope--flap">
  <svg class="flap" viewBox="0 0 342 149" preserveAspectRatio="none" aria-hidden="true">
    <path d="M0 0 L171 62 L342 0" fill="none" stroke="#d8d8d8" stroke-width="1"/>
  </svg>
  <div class="brand">RW Marlo Building Company LLC</div>
</section>

<section class="sheet envelope envelope--front">
  <div class="brand"><span class="mark"></span>RW Marlo Building Company LLC</div>
  <div class="contact small">
    4815 Brindlecove Road<br>
    Harlow Springs, NC 27099
  </div>
  <svg class="wave" viewBox="0 0 100 20" preserveAspectRatio="none" height="28">
    <path class="band-black" d="M0 10 C35 3 65 17 100 5 L100 20 L0 20 Z"/>
    <path class="band-red" d="M0 13 C35 7 65 20 100 9 L100 20 L0 20 Z"/>
  </svg>
</section>

</body>
</html>
```